Design für einen Jahresplaner gesucht
Zielgruppe
Scannen und Designen Zahntechnischer und Zahnmedizinischer Arbeiten und das Fräsen und 3d Drucken von bereits in CAD konstruierten Objekten. Wir verfügen über die modernsten Zahntechnischen Technologien und bieten diese als Dienstleister für Dentallabore an.
Aufgabenstellung
Wir benotigen ein Jahresplaner für unsere Kunden. Die Beigefügte Vorlage dient regelrecht nur der Grösenvorlage.
Das Design soll Technisch und Innovativ sein. Gleischzeitig aber gradlinig und nicht zu verspielt.
Das Logo kann ruhig stark ins Auge fallen. Die Schriftfarben sollen überwigen dunkelgrau sein. Hervorzuhebende Bereiche wie z. B. Sonntage, Feiertage sollten die Logofaben beinhalten. Bilder können auch verwendet werden aber wir würden uns über ein Schönes Layout ohne Bilder auch freuen.
PS: Unter dem Logo muss in Feiner Schrift stehen
eine Marke der Norvak GmbH

```html
<!DOCTYPE html>
<html lang="de">
<head>
<meta charset="utf-8">
<title>Jahresplaner 2019 – Dentavo</title>
<link href="https://fonts.googleapis.com/css2?family=PT+Sans+Narrow:wght@400;700&family=PT+Sans:wght@400;700&display=swap" rel="stylesheet">
<style>
  :root {
    --ground: #2b2a29;
    --cell: #ffffff;
    --weekend: #d9dadb;
    --holiday: #f8d08e;
    --blue: #2196d3;
    --purple: #a3308a;
    --ink: #2b2a29;
    --soft-text: #7a7a7a;
  }
  * { box-sizing: border-box; margin: 0; padding: 0; }
  html, body { width: 1200px; height: 840px; overflow: hidden; background: var(--ground); }
  .planner {
    position: relative; width: 1200px; height: 840px; overflow: hidden;
    background: var(--ground);
    font-family: "PT Sans Narrow", "PT Sans", sans-serif;
  }
  .year {
    position: absolute; left: 536px; top: 18px;
    font-family: "PT Sans", sans-serif; font-weight: 400;
    font-size: 106px; letter-spacing: 4px; color: #5f5f5e; line-height: 1;
  }
  .month { position: absolute; left: 0; width: 1200px; height: 80px; }
  .month-name {
    position: absolute; right: 1089px; top: 33px;
    color: #fff; font-weight: 700; font-size: 16px; letter-spacing: .2px;
  }
  .days { position: absolute; left: 121px; top: 0; display: flex; gap: 2px; }
  .day { width: 31px; }
  .dow {
    display: block; height: 18px; text-align: center;
    color: #fff; font-size: 14px; line-height: 18px;
  }
  .box {
    display: block; position: relative; height: 60px;
    background: var(--cell); text-align: center;
  }
  .num {
    display: block; padding-top: 3px;
    font-size: 21px; line-height: 24px; color: var(--ink); font-weight: 400;
  }
  .kw {
    position: absolute; left: 1px; top: 0;
    font-family: "PT Sans", sans-serif; font-weight: 700;
    font-size: 6px; line-height: 8px; color: var(--purple);
  }
  .note {
    position: absolute; left: 0; right: 0; bottom: 3px;
    font-family: "PT Sans Narrow", sans-serif;
    font-size: 5px; line-height: 6px; color: #555; text-transform: uppercase;
  }
  .hol .note { font-weight: 700; color: #6b5a3a; }
  .we .box { background: var(--weekend); }
  .we .num, .hol .num { color: var(--blue); font-weight: 700; }
  .hol .box { background: var(--holiday); }
  .empty .dow { color: #8a8a8a; }
  .empty .box { background: transparent; border: 1px solid #fff; }
  .tagline {
    position: absolute; left: 341px; top: 712px;
    font-family: "PT Sans", sans-serif; font-size: 12.5px; line-height: 16.5px;
    letter-spacing: 2.6px; color: var(--soft-text);
  }
  .mesh {
    position: absolute; left: 870px; top: 690px; width: 330px; height: 130px;
    background: radial-gradient(ellipse at 55% 50%, rgba(110,110,115,.35), rgba(43,42,41,0) 70%);
  }
  .brand {
    position: absolute; left: 722px; top: 712px;
    font-family: "PT Sans", sans-serif; font-weight: 700;
    font-size: 72px; line-height: 1; color: #5c5c5c; letter-spacing: -1px;
  }
  .brand-sub {
    position: absolute; left: 727px; top: 788px;
    font-family: "PT Sans", sans-serif; font-size: 17px; letter-spacing: .8px; color: #6e6e6e;
  }
</style>
</head>
<body>
<main class="planner">
  <div class="year">2019</div>

  <section class="month" style="top:151px">
    <h2 class="month-name">JULI</h2>
    <div class="days">
      <div class="day"><span class="dow">mo</span><span class="box"><span class="kw">27</span><span class="num">01</span></span></div>
      <div class="day"><span class="dow">di</span><span class="box"><span class="num">02</span></span></div>
      <div class="day"><span class="dow">mi</span><span class="box"><span class="num">03</span></span></div>
      <div class="day"><span class="dow">do</span><span class="box"><span class="num">04</span></span></div>
      <div class="day"><span class="dow">fr</span><span class="box"><span class="num">05</span></span></div>
      <div class="day we"><span class="dow">sa</span><span class="box"><span class="num">06</span></span></div>
      <div class="day we"><span class="dow">so</span><span class="box"><span class="num">07</span></span></div>
      <div class="day"><span class="dow">mo</span><span class="box"><span class="kw">28</span><span class="num">08</span></span></div>
      <div class="day"><span class="dow">di</span><span class="box"><span class="num">09</span></span></div>
      <div class="day"><span class="dow">mi</span><span class="box"><span class="num">10</span></span></div>
      <div class="day"><span class="dow">do</span><span class="box"><span class="num">11</span></span></div>
      <div class="day"><span class="dow">fr</span><span class="box" style="background:var(--weekend)"><span class="num">12</span></span></div>
      <div class="day we"><span class="dow">sa</span><span class="box"><span class="num">13</span></span></div>
      <div class="day we"><span class="dow">so</span><span class="box"><span class="num">14</span></span></div>
      <div class="day"><span class="dow">mo</span><span class="box"><span class="kw">29</span><span class="num">15</span></span></div>
      <div class="day"><span class="dow">di</span><span class="box"><span class="num">16</span></span></div>
      <div class="day"><span class="dow">mi</span><span class="box"><span class="num">17</span></span></div>
      <div class="day"><span class="dow">do</span><span class="box"><span class="num">18</span></span></div>
      <div class="day"><span class="dow">fr</span><span class="box"><span class="num">19</span></span></div>
      <div class="day we"><span class="dow">sa</span><span class="box"><span class="num">20</span></span></div>
      <div class="day we"><span class="dow">so</span><span class="box"><span class="num">21</span></span></div>
      <div class="day"><span class="dow">mo</span><span class="box"><span class="kw">30</span><span class="num">22</span></span></div>
      <div class="day"><span class="dow">di</span><span class="box"><span class="num">23</span></span></div>
      <div class="day"><span class="dow">mi</span><span class="box"><span class="num">24</span></span></div>
      <div class="day"><span class="dow">do</span><span class="box"><span class="num">25</span></span></div>
      <div class="day"><span class="dow">fr</span><span class="box"><span class="num">26</span></span></div>
      <div class="day we"><span class="dow">sa</span><span class="box"><span class="num">27</span></span></div>
      <div class="day we"><span class="dow">so</span><span class="box"><span class="num">28</span></span></div>
      <div class="day"><span class="dow">mo</span><span class="box"><span class="kw">31</span><span class="num">29</span></span></div>
      <div class="day"><span class="dow">di</span><span class="box"><span class="num">30</span></span></div>
      <div class="day"><span class="dow">mi</span><span class="box"><span class="num">31</span></span></div>
    </div>
  </section>

  <section class="month" style="top:241px">
    <h2 class="month-name">AUGUST</h2>
    <div class="days">
      <div class="day"><span class="dow">do</span><span class="box"><span class="kw">31</span><span class="num">01</span></span></div>
      <div class="day"><span class="dow">fr</span><span class="box"><span class="num">02</span></span></div>
      <div class="day we"><span class="dow">sa</span><span class="box"><span class="num">03</span></span></div>
      <div class="day we"><span class="dow">so</span><span class="box"><span class="num">04</span></span></div>
      <div class="day"><span class="dow">mo</span><span class="box"><span class="kw">32</span><span class="num">05</span></span></div>
      <div class="day"><span class="dow">di</span><span class="box"><span class="num">06</span></span></div>
      <div class="day"><span class="dow">mi</span><span class="box"><span class="num">07</span></span></div>
      <div class="day"><span class="dow">do</span><span class="box"><span class="num">08</span></span></div>
      <div class="day"><span class="dow">fr</span><span class="box"><span class="num">09</span></span></div>
      <div class="day we"><span class="dow">sa</span><span class="box"><span class="num">10</span></span></div>
      <div class="day we"><span class="dow">so</span><span class="box"><span class="num">11</span></span></div>
      <div class="day"><span class="dow">mo</span><span class="box"><span class="kw">33</span><span class="num">12</span></span></div>
      <div class="day"><span class="dow">di</span><span class="box"><span class="num">13</span></span></div>
      <div class="day"><span class="dow">mi</span><span class="box"><span class="num">14</span></span></div>
      <div class="day hol"><span class="dow">do</span><span class="box"><span class="num">15</span><span class="note">Maria<br>Himmel<br>fahrt</span></span></div>
      <div class="day"><span class="dow">fr</span><span class="box"><span class="num">16</span></span></div>
      <div class="day we"><span class="dow">sa</span><span class="box"><span class="num">17</span></span></div>
      <div class="day we"><span class="dow">so</span><span class="box"><span class="num">18</span></span></div>
      <div class="day"><span class="dow">mo</span><span class="box"><span class="kw">34</span><span class="num">19</span></span></div>
      <div class="day"><span class="dow">di</span><span class="box"><span class="num">20</span></span></div>
      <div class="day"><span class="dow">mi</span><span class="box"><span class="num">21</span></span></div>
      <div class="day"><span class="dow">do</span><span class="box"><span class="num">22</span></span></div>
      <div class="day"><span class="dow">fr</span><span class="box"><span class="num">23</span></span></div>
      <div class="day we"><span class="dow">sa</span><span class="box"><span class="num">24</span></span></div>
      <div class="day we"><span class="dow">so</span><span class="box"><span class="num">25</span></span></div>
      <div class="day"><span class="dow">mo</span><span class="box"><span class="kw">35</span><span class="num">26</span></span></div>
      <div class="day"><span class="dow">di</span><span class="box"><span class="num">27</span></span></div>
      <div class="day"><span class="dow">mi</span><span class="box"><span class="num">28</span></span></div>
      <div class="day"><span class="dow">do</span><span class="box"><span class="num">29</span></span></div>
      <div class="day"><span class="dow">fr</span><span class="box"><span class="num">30</span></span></div>
      <div class="day we"><span class="dow">sa</span><span class="box"><span class="num">31</span></span></div>
    </div>
  </section>

  <section class="month" style="top:331px">
    <h2 class="month-name">SEPTEMBER</h2>
    <div class="days">
      <div class="day we"><span class="dow">so</span><span class="box"><span class="kw">35</span><span class="num">01</span></span></div>
      <div class="day"><span class="dow">mo</span><span class="box"><span class="kw">36</span><span class="num">02</span></span></div>
      <div class="day"><span class="dow">di</span><span class="box"><span class="num">03</span></span></div>
      <div class="day"><span class="dow">mi</span><span class="box"><span class="num">04</span></span></div>
      <div class="day"><span class="dow">do</span><span class="box"><span class="num">05</span></span></div>
      <div class="day"><span class="dow">fr</span><span class="box"><span class="num">06</span></span></div>
      <div class="day we"><span class="dow">sa</span><span class="box"><span class="num">07</span></span></div>
      <div class="day we"><span class="dow">so</span><span class="box"><span class="num">08</span></span></div>
      <div class="day"><span class="dow">mo</span><span class="box"><span class="kw">37</span><span class="num">09</span></span></div>
      <div class="day"><span class="dow">di</span><span class="box"><span class="num">10</span></span></div>
      <div class="day"><span class="dow">mi</span><span class="box"><span class="num">11</span></span></div>
      <div class="day"><span class="dow">do</span><span class="box"><span class="num">12</span></span></div>
      <div class="day"><span class="dow">fr</span><span class="box"><span class="num">13</span></span></div>
      <div class="day we"><span class="dow">sa</span><span class="box"><span class="num">14</span></span></div>
      <div class="day we"><span class="dow">so</span><span class="box"><span class="num">15</span></span></div>
      <div class="day"><span class="dow">mo</span><span class="box"><span class="kw">38</span><span class="num">16</span></span></div>
      <div class="day"><span class="dow">di</span><span class="box"><span class="num">17</span></span></div>
      <div class="day"><span class="dow">mi</span><span class="box"><span class="num">18</span></span></div>
      <div class="day"><span class="dow">do</span><span class="box"><span class="num">19</span></span></div>
      <div class="day"><span class="dow">fr</span><span class="box"><span class="num">20</span></span></div>
      <div class="day we"><span class="dow">sa</span><span class="box"><span class="num">21</span></span></div>
      <div class="day we"><span class="dow">so</span><span class="box"><span class="num">22</span></span></div>
      <div class="day"><span class="dow">mo</span><span class="box"><span class="kw">39</span><span class="num">23</span></span></div>
      <div class="day"><span class="dow">di</span><span class="box"><span class="num">24</span></span></div>
      <div class="day"><span class="dow">mi</span><span class="box"><span class="num">25</span></span></div>
      <div class="day"><span class="dow">do</span><span class="box"><span class="num">26</span></span></div>
      <div class="day"><span class="dow">fr</span><span class="box"><span class="num">27</span></span></div>
      <div class="day we"><span class="dow">sa</span><span class="box"><span class="num">28</span></span></div>
      <div class="day we"><span class="dow">so</span><span class="box"><span class="num">29</span></span></div>
      <div class="day"><span class="dow">mo</span><span class="box"><span class="kw">40</span><span class="num">30</span></span></div>
      <div class="day empty"><span class="dow">di</span><span class="box"></span></div>
    </div>
  </section>

  <section class="month" style="top:421px">
    <h2 class="month-name">OKTOBER</h2>
    <div class="days">
      <div class="day"><span class="dow">di</span><span class="box"><span class="kw">40</span><span class="num">01</span></span></div>
      <div class="day"><span class="dow">mi</span><span class="box"><span class="num">02</span></span></div>
      <div class="day hol"><span class="dow">do</span><span class="box"><span class="num">03</span><span class="note">Tag der<br>Dt. Einheit</span></span></div>
      <div class="day"><span class="dow">fr</span><span class="box"><span class="num">04</span></span></div>
      <div class="day we"><span class="dow">sa</span><span class="box"><span class="num">05</span></span></div>
      <div class="day we"><span class="dow">so</span><span class="box"><span class="num">06</span><span class="note">Erntedank</span></span></div>
      <div class="day"><span class="dow">mo</span><span class="box"><span class="kw">41</span><span class="num">07</span></span></div>
      <div class="day"><span class="dow">di</span><span class="box"><span class="num">08</span></span></div>
      <div class="day"><span class="dow">mi</span><span class="box"><span class="num">09</span></span></div>
      <div class="day"><span class="dow">do</span><span class="box"><span class="num">10</span></span></div>
      <div class="day"><span class="dow">fr</span><span class="box"><span class="num">11</span></span></div>
      <div class="day we"><span class="dow">sa</span><span class="box"><span class="num">12</span></span></div>
      <div class="day we"><span class="dow">so</span><span class="box"><span class="num">13</span></span></div>
      <div class="day"><span class="dow">mo</span><span class="box"><span class="kw">42</span><span class="num">14</span></span></div>
      <div class="day"><span class="dow">di</span><span class="box"><span class="num">15</span></span></div>
      <div class="day"><span class="dow">mi</span><span class="box"><span class="num">16</span></span></div>
      <div class="day"><span class="dow">do</span><span class="box"><span class="num">17</span></span></div>
      <div class="day"><span class="dow">fr</span><span class="box"><span class="num">18</span></span></div>
      <div class="day we"><span class="dow">sa</span><span class="box"><span class="num">19</span></span></div>
      <div class="day we"><span class="dow">so</span><span class="box"><span class="num">20</span></span></div>
      <div class="day"><span class="dow">mo</span><span class="box"><span class="kw">43</span><span class="num">21</span></span></div>
      <div class="day"><span class="dow">di</span><span class="box"><span class="num">22</span></span></div>
      <div class="day"><span class="dow">mi</span><span class="box"><span class="num">23</span></span></div>
      <div class="day"><span class="dow">do</span><span class="box"><span class="num">24</span></span></div>
      <div class="day"><span class="dow">fr</span><span class="box"><span class="num">25</span></span></div>
      <div class="day we"><span class="dow">sa</span><span class="box"><span class="num">26</span></span></div>
      <div class="day we"><span class="dow">so</span><span class="box"><span class="num">27</span><span class="note">Ende der<br>Sommerzeit</span></span></div>
      <div class="day"><span class="dow">mo</span><span class="box"><span class="kw">44</span><span class="num">28</span></span></div>
      <div class="day"><span class="dow">di</span><span class="box"><span class="num">29</span></span></div>
      <div class="day"><span class="dow">mi</span><span class="box"><span class="num">30</span></span></div>
      <div class="day"><span class="dow">do</span><span class="box"><span class="num">31</span><span class="note">Reforma-<br>tions<br>Tag</span></span></div>
    </div>
  </section>

  <section class="month" style="top:511px">
    <h2 class="month-name">NOVEMBER</h2>
    <div class="days">
      <div class="day hol"><span class="dow">fr</span><span class="box"><span class="kw">44</span><span class="num">01</span><span class="note">Aller<br>Heiligen</span></span></div>
      <div class="day we"><span class="dow">sa</span><span class="box"><span class="num">02</span><span class="note" style="font-weight:700">Aller<br>Seelen</span></span></div>
      <div class="day we"><span class="dow">so</span><span class="box"><span class="num">03</span></span></div>
      <div class="day"><span class="dow">mo</span><span class="box"><span class="kw">45</span><span class="num">04</span></span></div>
      <div class="day"><span class="dow">di</span><span class="box"><span class="num">05</span></span></div>
      <div class="day"><span class="dow">mi</span><span class="box"><span class="num">06</span></span></div>
      <div class="day"><span class="dow">do</span><span class="box"><span class="num">07</span></span></div>
      <div class="day"><span class="dow">fr</span><span class="box"><span class="num">08</span></span></div>
      <div class="day we"><span class="dow">sa</span><span class="box"><span class="num">09</span></span></div>
      <div class="day we"><span class="dow">so</span><span class="box"><span class="num">10</span></span></div>
      <div class="day"><span class="dow">mo</span><span class="box"><span class="kw">46</span><span class="num">11</span></span></div>
      <div class="day"><span class="dow">di</span><span class="box"><span class="num">12</span></span></div>
      <div class="day"><span class="dow">mi</span><span class="box"><span class="num">13</span></span></div>
      <div class="day"><span class="dow">do</span><span class="box"><span class="num">14</span></span></div>
      <div class="day"><span class="dow">fr</span><span class="box"><span class="num">15</span></span></div>
      <div class="day we"><span class="dow">sa</span><span class="box"><span class="num">16</span></span></div>
      <div class="day we"><span class="dow">so</span><span class="box"><span class="num">17</span><span class="note">Volks<br>Trauer<br>Tag</span></span></div>
      <div class="day"><span class="dow">mo</span><span class="box"><span class="kw">47</span><span class="num">18</span></span></div>
      <div class="day"><span class="dow">di</span><span class="box"><span class="num">19</span></span></div>
      <div class="day"><span class="dow">mi</span><span class="box"><span class="num">20</span><span class="note">Buss- und<br>Bettag</span></span></div>
      <div class="day"><span class="dow">do</span><span class="box"><span class="num">21</span></span></div>
      <div class="day"><span class="dow">fr</span><span class="box"><span class="num">22</span></span></div>
      <div class="day we"><span class="dow">sa</span><span class="box"><span class="num">23</span></span></div>
      <div class="day we"><span class="dow">so</span><span class="box"><span class="num">24</span><span class="note">Toten<br>Sonntag</span></span></div>
      <div class="day"><span class="dow">mo</span><span class="box"><span class="kw">48</span><span class="num">25</span></span></div>
      <div class="day"><span class="dow">di</span><span class="box"><span class="num">26</span></span></div>
      <div class="day"><span class="dow">mi</span><span class="box"><span class="num">27</span></span></div>
      <div class="day"><span class="dow">do</span><span class="box"><span class="num">28</span></span></div>
      <div class="day"><span class="dow">fr</span><span class="box"><span class="num">29</span></span></div>
      <div class="day we"><span class="dow">sa</span><span class="box"><span class="num">30</span></span></div>
      <div class="day empty"><span class="dow">so</span><span class="box"></span></div>
    </div>
  </section>

  <section class="month" style="top:601px">
    <h2 class="month-name">DEZEMBER</h2>
    <div class="days">
      <div class="day we"><span class="dow">so</span><span class="box"><span class="kw">48</span><span class="num">01</span><span class="note">1. Advent</span></span></div>
      <div class="day"><span class="dow">mo</span><span class="box"><span class="kw">49</span><span class="num">02</span></span></div>
      <div class="day"><span class="dow">di</span><span class="box"><span class="num">03</span></span></div>
      <div class="day"><span class="dow">mi</span><span class="box"><span class="num">04</span></span></div>
      <div class="day"><span class="dow">do</span><span class="box"><span class="num">05</span></span></div>
      <div class="day"><span class="dow">fr</span><span class="box"><span class="num">06</span></span></div>
      <div class="day we"><span class="dow">sa</span><span class="box"><span class="num">07</span></span></div>
      <div class="day we"><span class="dow">so</span><span class="box"><span class="num">08</span><span class="note">2. Advent</span></span></div>
      <div class="day"><span class="dow">mo</span><span class="box"><span class="kw">50</span><span class="num">09</span></span></div>
      <div class="day"><span class="dow">di</span><span class="box"><span class="num">10</span></span></div>
      <div class="day"><span class="dow">mi</span><span class="box"><span class="num">11</span></span></div>
      <div class="day"><span class="dow">do</span><span class="box"><span class="num">12</span></span></div>
      <div class="day"><span class="dow">fr</span><span class="box"><span class="num">13</span></span></div>
      <div class="day we"><span class="dow">sa</span><span class="box"><span class="num">14</span></span></div>
      <div class="day we"><span class="dow">so</span><span class="box"><span class="num">15</span><span class="note">3. Advent</span></span></div>
      <div class="day"><span class="dow">mo</span><span class="box"><span class="kw">51</span><span class="num">16</span></span></div>
      <div class="day"><span class="dow">di</span><span class="box"><span class="num">17</span></span></div>
      <div class="day"><span class="dow">mi</span><span class="box"><span class="num">18</span></span></div>
      <div class="day"><span class="dow">do</span><span class="box"><span class="num">19</span></span></div>
      <div class="day"><span class="dow">fr</span><span class="box"><span class="num">20</span></span></div>
      <div class="day we"><span class="dow">sa</span><span class="box"><span class="num">21</span></span></div>
      <div class="day we"><span class="dow">so</span><span class="box"><span class="num">22</span><span class="note">4. Advent</span></span></div>
      <div class="day"><span class="dow">mo</span><span class="box"><span class="kw">52</span><span class="num">23</span></span></div>
      <div class="day"><span class="dow">di</span><span class="box"><span class="num">24</span><span class="note">Heilig<br>Abend</span></span></div>
      <div class="day hol"><span class="dow">mi</span><span class="box"><span class="num">25</span><span class="note">1.<br>Weihnachts<br>Feiertag</span></span></div>
      <div class="day hol"><span class="dow">do</span><span class="box"><span class="num">26</span><span class="note">2.<br>Weihnachts<br>Feiertag</span></span></div>
      <div class="day"><span class="dow">fr</span><span class="box"><span class="num">27</span></span></div>
      <div class="day we"><span class="dow">sa</span><span class="box"><span class="num">28</span></span></div>
      <div class="day we"><span class="dow">so</span><span class="box"><span class="num">29</span></span></div>
      <div class="day"><span class="dow">mo</span><span class="box"><span class="kw">01</span><span class="num">30</span></span></div>
      <div class="day"><span class="dow">di</span><span class="box"><span class="num">31</span><span class="note">Sylvester</span></span></div>
    </div>
  </section>

  <p class="tagline">Scannen und designen zahntechnischer<br>und zahnmedizinischer Arbeiten<br>Fräsen und 3D-Drucken von<br>in CAD konstruierten Objekten</p>

  <div class="mesh" role="img" aria-label="Dezente Drahtgitter-Darstellung eines gefrästen Zahnmodells"></div>
  <div class="brand">Dentavo</div>
  <p class="brand-sub">eine Gruppe der Norvak GmbH</p>
</main>
</body>
</html>
```